KV Taxidermy

I need business Cards with my logo and a background photo of one of my taxidermy mounts.
I would like a black back drop behind it all and what ever looks best for my contact information (red or white?)
Marcus Pellow
555-218-4907
kvtaxidermy512@mailvex.net
Chatterly page

```html
<!DOCTYPE html>
<html lang="en">
<head>
<meta charset="utf-8">
<title>KV Taxidermy – Business Card</title>
<link rel="stylesheet" href="https://fonts.googleapis.com/css2?family=Exo+2:wght@400;700&display=swap">
<style>
  :root {
    --backdrop: #161616;
    --card: #0a0a0a;
    --mount-light: #5a5a58;
    --mount-dark: #1c1c1c;
    --accent-red: #e0242b;
    --text-white: #f2f2f2;
    --rule: #8a8a8a;
  }
  * { margin: 0; padding: 0; box-sizing: border-box; }
  html, body {
    width: 1200px; height: 1200px; overflow: hidden;
    background: radial-gradient(circle at 50% 45%, #222 0%, var(--backdrop) 70%);
    font-family: "Exo 2", sans-serif;
  }
  .stage {
    width: 1200px; height: 1200px;
    display: flex; align-items: center; justify-content: center;
  }
  .business-card {
    position: relative;
    width: 1050px; height: 600px;
    background: var(--card);
    border-radius: 28px;
    overflow: hidden;
    box-shadow: 0 20px 50px rgba(0,0,0,.6);
  }
  .mount-photo {
    position: absolute;
    left: 430px; top: 40px;
    width: 590px; height: 540px;
    border-radius: 40% 45% 20% 25% / 30% 35% 40% 45%;
    background: linear-gradient(180deg, var(--mount-light) 0%, #3a3a39 45%, var(--mount-dark) 100%);
    opacity: .55;
  }
  .brand-mark {
    position: absolute;
    left: 60px; top: 270px;
    display: flex; align-items: center; gap: 14px;
    color: var(--text-white);
    font-weight: 700;
    font-size: 33px;
    letter-spacing: 3px;
    text-transform: uppercase;
    white-space: nowrap;
  }
  .brand-mark .brand-square {
    width: 24px; height: 24px;
    background: var(--text-white);
  }
  .divider {
    position: absolute;
    left: 0; top: 0;
    width: 1050px; height: 600px;
  }
  .contact-block {
    position: absolute;
    left: 490px; top: 215px;
    color: var(--text-white);
  }
  .contact-name {
    color: var(--accent-red);
    font-weight: 700;
    font-size: 44px;
    letter-spacing: 3px;
    text-transform: uppercase;
    margin-bottom: 10px;
    white-space: nowrap;
  }
  .contact-list { list-style: none; }
  .contact-item {
    display: flex; align-items: center; gap: 14px;
    font-size: 27px;
    letter-spacing: 1.5px;
    line-height: 40px;
    white-space: nowrap;
  }
  .contact-icon { width: 26px; height: 28px; flex: none; }
</style>
</head>
<body>
<main class="stage">
  <article class="business-card">
    <div class="mount-photo" role="img" aria-label="Background photo of a white ram taxidermy mount lying on a rock"></div>

    <div class="brand-mark">
      <span class="brand-square"></span>
      <span class="brand-name">KV Taxidermy</span>
    </div>

    <svg class="divider" viewBox="0 0 1050 600" aria-hidden="true">
      <line x1="460" y1="135" x2="420" y2="470" stroke="var(--rule)" stroke-width="2"/>
    </svg>

    <section class="contact-block">
      <h1 class="contact-name">Marcus Pellow</h1>
      <ul class="contact-list">
        <li class="contact-item">
          <svg class="contact-icon" viewBox="0 0 26 28" aria-hidden="true">
            <polygon points="13,1 25,7.5 25,20.5 13,27 1,20.5 1,7.5" fill="none" stroke="#fff" stroke-width="2"/>
            <path d="M9 8 l3 3 -1.5 1.5 q1.5 3 4 4 l1.5 -1.5 3 3 -2 2 q-6 -1 -10 -8z" fill="#fff"/>
          </svg>
          <span>555-218-4907</span>
        </li>
        <li class="contact-item">
          <svg class="contact-icon" viewBox="0 0 26 28" aria-hidden="true">
            <polygon points="13,1 25,7.5 25,20.5 13,27 1,20.5 1,7.5" fill="none" stroke="#fff" stroke-width="2"/>
            <rect x="7" y="10" width="12" height="8" fill="none" stroke="#fff" stroke-width="1.6"/>
            <path d="M7 10 l6 5 6 -5" fill="none" stroke="#fff" stroke-width="1.6"/>
          </svg>
          <span>kvtaxidermy512@mailvex.net</span>
        </li>
        <li class="contact-item">
          <svg class="contact-icon" viewBox="0 0 26 28" aria-hidden="true">
            <polygon points="13,1 25,7.5 25,20.5 13,27 1,20.5 1,7.5" fill="none" stroke="#fff" stroke-width="2"/>
          </svg>
          <span>kvtaxidermy</span>
        </li>
      </ul>
    </section>
  </article>
</main>
</body>
</html>
```